pasmuro.com

Develop a website for pasmura.com will be a site to sell tickets for concerts, shows, shows, theaters and others. I need a web design easy view, very easy to use and accumulate events by date. The aim is to develop the site was connected to a complex system that is already developed. (Important this page to a robust system was connected via links the idea is to develop only the front view)
Updates

Reason: I need more designs yet we have not made the decision

Target Market(s)

millennials, adults, who want to enjoy concerts and shows

Industry/Entity Type

Event

Number of Pages Required

5+ page

Colors
1b1b1b
aaaaaa
ffffff

Requirements
Must have
• Easy Vista, accumulation of upcoming events, past events. The tabs should have are: 1 Start: In this part of upcoming events occur. You could put a banner on the top and down the events by date. 2. How to order: page with instructions on how to purchase tickets 3. About Us: The company history 4. Contact: Phones and template for contact by mail 5. Our policies: shopping 6. Notice Privacy: Privacy Notice Copoy 7. Centers Sale: physical places where they can purchase tickets Promoters 8. access: Link to a template
Nice to have
• as you can see p www.volandrimexa.com or crunvía.com or crunvea.com or plovindex.com (important this page to a robust system was connected via links the idea is to develop only the front view)
Should not have
• Many things Tangled

```html
<!DOCTYPE html>
<html lang="es">
<head>
<meta charset="utf-8">
<title>Pasmura – Inicio</title>
<link rel="stylesheet" href="https://fonts.googleapis.com/css2?family=Open+Sans:wght@400;600;700;800&family=Josefin+Sans:wght@400&display=swap">
<style>
:root{
  --black:#000;
  --ink:#1b1b1b;
  --grey:#aaaaaa;
  --white:#ffffff;
  --yellow:#ffe934;
  --line:rgba(255,255,255,.35);
}
*{margin:0;padding:0;box-sizing:border-box}
html,body{width:1200px;height:2317px;overflow:hidden;background:var(--black)}
body{font-family:"Open Sans",Arial,sans-serif;color:var(--white);position:relative}

.site-header{position:absolute;left:0;top:0;width:1200px;height:91px;background:var(--black)}
.brand{position:absolute;top:14px;left:0;width:100%;text-align:center;font-size:27px;font-weight:400;letter-spacing:.5px}
.main-nav{position:absolute;top:63px;left:0;width:100%;display:flex;justify-content:center;gap:38px;font-family:"Josefin Sans",Arial,sans-serif;font-size:14px}
.main-nav a{color:var(--white);text-decoration:none}
.main-nav a.is-active{color:var(--yellow)}

.hero{position:absolute;left:0;top:91px;width:1200px;height:605px;overflow:hidden}
.hero-photo{position:absolute;inset:0;background:radial-gradient(ellipse at 60% 35%,#6a3a2c 0%,#3a1c16 35%,#160c0a 70%,#0a0606 100%)}
.hero-date{position:absolute;left:0;top:221px;width:302px;height:168px;background:var(--yellow);color:var(--black);font-weight:800;font-size:98px;line-height:168px;padding-left:36px;letter-spacing:-2px}
.hero-band{position:absolute;left:0;top:389px;width:1200px;height:216px;background:rgba(0,0,0,.55)}
.hero-title{position:absolute;left:42px;top:412px;width:700px;color:var(--yellow);font-size:31px;font-weight:700;line-height:40px}
.hero-text{position:absolute;left:42px;top:504px;width:690px;font-size:16px;line-height:20px}
.btn-buy-lg{position:absolute;left:792px;top:463px;width:295px;height:89px;border:3px solid var(--white);font-size:31px;font-weight:600;text-align:center;line-height:83px}

.event-cards{position:absolute;left:0;top:696px;width:1200px;height:465px;display:flex;background:var(--black)}
.event-card{width:240px;height:465px;position:relative}
.card-photo{position:absolute;left:0;top:0;width:240px;height:202px}
.card-date{position:absolute;left:14px;bottom:-6px;font-size:62px;font-weight:700;letter-spacing:-1px;line-height:1}
.card-title{position:absolute;left:19px;top:214px;width:221px;color:var(--yellow);font-size:15px;font-weight:700;line-height:20px;letter-spacing:-.1px;text-transform:uppercase;white-space:nowrap}
.card-text{position:absolute;left:19px;top:326px;width:215px;font-size:12.5px;line-height:16px}
.card-more{position:absolute;left:19px;top:418px;color:var(--yellow);font-size:16px;font-weight:700}

.tour{position:absolute;left:0;top:1161px;width:1200px;height:776px;background:radial-gradient(ellipse at 55% 40%,#2a2a2a 0%,#171717 45%,#0b0b0b 100%)}
.tour-list{position:absolute;left:60px;top:66px;width:1079px;list-style:none}
.tour-row{height:120px;border-bottom:1.5px solid var(--line);display:flex;align-items:center;position:relative}
.tour-day{width:124px;padding-left:28px;font-size:60px;font-weight:700;letter-spacing:-1px}
.tour-when{width:82px;font-size:21px;font-weight:600;line-height:27px;text-align:center}
.tour-divider{width:2px;height:64px;background:var(--line);margin:0 30px 0 0}
.tour-venue{font-size:22.5px;font-weight:700}
.btn-buy{position:absolute;right:30px;top:34px;width:154px;height:57px;border:2.5px solid var(--white);font-size:22px;font-weight:600;text-align:center;line-height:52px}
.sold-out{position:absolute;right:50px;top:0;line-height:120px;font-size:22px;font-weight:600;color:var(--grey)}

.site-footer{position:absolute;left:0;top:1937px;width:1200px;height:380px;background:var(--black)}
.footer-col{position:absolute;top:84px}
.footer-col h3{font-size:22px;font-weight:700;margin-bottom:26px}
.col-location{left:131px}
.col-location address{font-style:normal;font-size:22px;line-height:27px}
.col-posts{left:518px}
.post{display:flex;align-items:center;margin-bottom:15px}
.post-thumb{width:53px;height:53px;background:linear-gradient(135deg,#5a4a44,#1f1a18)}
.post-title{margin-left:27px;font-size:15px;font-weight:700;line-height:17px}
.post-date{display:block;font-size:11.5px;color:var(--grey)}
.col-feed{left:849px;width:240px}
.feed-item{font-size:12.5px;line-height:15.5px;margin-bottom:18px}
.feed-item b{font-weight:700}
.feed-age{display:block;font-size:15px;font-weight:700;color:var(--grey)}
</style>
</head>
<body>

<header class="site-header">
  <div class="brand">Pasmura</div>
  <nav class="main-nav">
    <a class="is-active" href="#">Inicio</a>
    <a href="#">Cómo comprar</a>
    <a href="#">Quiénes Somos</a>
    <a href="#">Contáctanos</a>
    <a href="#">Nuestras Políticas</a>
    <a href="#">Aviso de Privacidad</a>
    <a href="#">Centros de Venta</a>
    <a href="#">Acceso a Promotores</a>
  </nav>
</header>

<section class="hero">
  <div class="hero-photo" role="img" aria-label="Concert photo: a singer on stage pointing to the crowd under red lights"></div>
  <div class="hero-date">27/9</div>
  <div class="hero-band"></div>
  <h1 class="hero-title">Etiam pellentesque eros a neque facilisis eleifend. Aenean in nisl risus.</h1>
  <p class="hero-text">Aliquam risus turpis, dignissim eget vehicula eget, accumsan eu magna. Proin semper nisl magna, quis lacinia augue fringilla eget. Aliquam tellus leo, aliquam sit amet lorem non, laoreet sodales mi.</p>
  <div class="btn-buy-lg">COMPRAR</div>
</section>

<section class="event-cards">
  <article class="event-card">
    <div class="card-photo" role="img" aria-label="Portrait of a young male artist in a green jacket" style="background:linear-gradient(160deg,#6b6157,#2f4a36 70%,#1d2a20)"><span class="card-date">17/4</span></div>
    <h2 class="card-title">Lorem ipsum dolor<br>sit amet conse ctetur<br>adipisicinlorem ipsum<br>dolor sit amet conse<br>ctetur adipisicin</h2>
    <p class="card-text">Aliquam risus turpis, dignissim eget vehicula eget, accumsan eu magna. Proin semper nisl magna, quis lacinia augue fringilla eget.</p>
    <div class="card-more">LEER MAS...</div>
  </article>
  <article class="event-card">
    <div class="card-photo" role="img" aria-label="Portrait of a young female artist with long hair" style="background:linear-gradient(160deg,#8a7a62,#6a4a32 60%,#3a2a1e)"><span class="card-date">10/5</span></div>
    <h2 class="card-title">Etiam pellentesque<br>eros a neque facilisis<br>eleifend. Aenean in<br>nisl risus. Nam asaf<br>lobortis.</h2>
    <p class="card-text">Aliquam risus turpis, dignissim eget vehicula eget, accumsan eu magna. Proin semper nisl magna, quis lacinia augue fringilla eget.</p>
    <div class="card-more">READ MORE...</div>
  </article>
  <article class="event-card">
    <div class="card-photo" role="img" aria-label="Portrait of a female artist with braids in a blue jacket" style="background:linear-gradient(160deg,#9a9a90,#4a4a4a 55%,#2a3a6a)"><span class="card-date">7/6</span></div>
    <h2 class="card-title">Sed purus sem, gravi-<br>da nec rhoncus quis,<br>aliquet quis nisi. Ut<br>consequat justo id<br>nibh fermentum.</h2>
    <p class="card-text">Aliquam risus turpis, dignissim eget vehicula eget, accumsan eu magna. Proin semper nisl magna, quis lacinia augue fringilla eget.</p>
    <div class="card-more">READ MORE...</div>
  </article>
  <article class="event-card">
    <div class="card-photo" role="img" aria-label="Portrait of a blonde female singer holding a microphone" style="background:linear-gradient(160deg,#5a6a9a,#c8a878 55%,#6a3a3a)"><span class="card-date">12/7</span></div>
    <h2 class="card-title">Vestibulum venena-<br>tis, augue in rhoncus<br>lacinia, risus eros<br>pharetra ante, nec<br>accumsan lacus.</h2>
    <p class="card-text">Aliquam risus turpis, dignissim eget vehicula eget, accumsan eu magna. Proin semper nisl magna, quis lacinia augue fringilla eget.</p>
    <div class="card-more">READ MORE...</div>
  </article>
  <article class="event-card">
    <div class="card-photo" role="img" aria-label="Portrait of a young male artist in a green jacket" style="background:linear-gradient(160deg,#6b6157,#2f4a36 70%,#1d2a20)"><span class="card-date">3/8</span></div>
    <h2 class="card-title">Lorem ipsum dolor<br>sit amet conse ctetur<br>adipisicinlorem ipsum<br>dolor sit amet conse<br>ctetur adipisicin</h2>
    <p class="card-text">Aliquam risus turpis, dignissim eget vehicula eget, accumsan eu magna. Proin semper nisl magna, quis lacinia augue fringilla eget.</p>
    <div class="card-more">READ MORE...</div>
  </article>
</section>

<section class="tour" role="img" aria-label="Dark background photo of a performer with a microphone and blurred stage lights">
  <ul class="tour-list">
    <li class="tour-row"><span class="tour-day">10</span><span class="tour-when">May<br>Jue</span><span class="tour-divider"></span><span class="tour-venue">Velmora Open Air – Norvalia</span><span class="sold-out">AGOTADO!</span></li>
    <li class="tour-row"><span class="tour-day">04</span><span class="tour-when">Jun<br>Vie</span><span class="tour-divider"></span><span class="tour-venue">Ostrava Bay – Lumen Arena</span><span class="btn-buy">COMPRAR</span></li>
    <li class="tour-row"><span class="tour-day">14</span><span class="tour-when">Jul<br>Sab</span><span class="tour-divider"></span><span class="tour-venue">Castelmoor – Greenfold Fest</span><span class="btn-buy">COMPRAR</span></li>
    <li class="tour-row"><span class="tour-day">27</span><span class="tour-when">Ago<br>Sab</span><span class="tour-divider"></span><span class="tour-venue">Tarnvik – Polaris Hall</span><span class="btn-buy">COMPRAR</span></li>
    <li class="tour-row"><span class="tour-day">25</span><span class="tour-when">Sep<br>Jue</span><span class="tour-divider"></span><span class="tour-venue">Brevanta – Corvel Dome</span><span class="sold-out">AGOTADO!</span></li>
  </ul>
</section>

<footer class="site-footer">
  <div class="footer-col col-location">
    <h3>Localizacion</h3>
    <address>Pasmura<br>48 Larchmont Way<br>Dunmore, OR 97210<br>T: +9000555018<br>Email: hola@pasmura.com<br>www.pasmura.com</address>
  </div>
  <div class="footer-col col-posts">
    <h3>Ultimos Posts</h3>
    <div class="post"><div class="post-thumb" role="img" aria-label="Post thumbnail photo of an artist"></div><div class="post-title">Music Heals<span class="post-date">Sep 28, 2016</span></div></div>
    <div class="post"><div class="post-thumb" role="img" aria-label="Post thumbnail photo of an artist"></div><div class="post-title">Music Heals<span class="post-date">Sep 30, 2016</span></div></div>
    <div class="post"><div class="post-thumb" role="img" aria-label="Post thumbnail photo of an artist"></div><div class="post-title">Music Heals<span class="post-date">Sep 28, 2016</span></div></div>
  </div>
  <div class="footer-col col-feed">
    <h3>Chirpa</h3>
    <p class="feed-item">Check out Lumo - A modern #PressKit theme for digital art: https://lnk.ex/a7Kq2<span class="feed-age">1 year ago</span></p>
    <p class="feed-item"><b>Create an amazing website today with Brisk - A Personal, Professional, Advanced #PressKit Theme: https://lnk.ex/b9Tr4</b><span class="feed-age">1 year ago</span></p>
  </div>
</footer>

</body>
</html>
```